Accountability Project Graphics

I want to create 10 social media graphics (new Instagram size 4:5 (1080 x 1350 pixels) focusing on our Kelmora Accountability App, using any of the 3 pictures attached. Use the attached pics only, NO RANDOM STOCK PHOTOGRAPHY. For the color scheme, use the landing page colors/fonts (attached).
You can add any of the 3 photos attached but I mainly need BOLD text that includes these headlines and sub-headlines on them.
Please NOTE for all the headlines below, also add this sub-headline on each graphic:
Stay Consistent with MB in Your Pocket!
Here are the headlines:
• Stop Starting Over Every Monday
• You don't need more willpower. You need more support
• Built for women who are tired of doing this alone
• When Motivation Fades, MB Checks In
• The Support System You've Been Missing
• Support When Motivation Disappears
• What if MB Checked in Every Day?
• The Missing Piece Isn't Another Diet
• Eat the food you love. Stay accountable every day.
• One Bad Meal Doesn't Mean You Failed
women over 40 trying to lose weight

```html
<!DOCTYPE html>
<html lang="en">
<head>
<meta charset="utf-8">
<title>Kelmora Accountability App – Social Graphics</title>
<link rel="stylesheet" href="https://fonts.googleapis.com/css2?family=Playfair+Display:ital,wght@0,900;1,900&family=Poppins:wght@600;700&display=swap">
<style>
:root{
  --stage:#8e8f92;
  --blush:#fbe4eb;
  --blush-soft:#fdf1f4;
  --blush-deep:#f6c9d8;
  --plum:#2a1233;
  --plum-bar:#4a1a43;
  --rose:#cc3f70;
  --white:#ffffff;
  --ink:#1c1c1c;
  --photo-dark:#2a2a40;
  --photo-denim:#3e5273;
  --photo-pink:#c44d7f;
  --photo-lime:#e3eab0;
}
*{box-sizing:border-box;margin:0;padding:0}
html,body{width:1200px;height:1200px;overflow:hidden;background:var(--stage)}
.board{position:relative;width:1200px;height:1200px}
.card{position:absolute;width:259px;height:324px;overflow:hidden;
  background:linear-gradient(160deg,var(--blush-soft) 0%,var(--blush) 60%,#f9dbe5 100%);
  box-shadow:0 4px 10px rgba(0,0,0,.22)}
.card::before{content:"";position:absolute;right:-40px;top:-70px;width:190px;height:190px;border-radius:50%;background:var(--blush-deep);opacity:.55}
.photo{position:absolute;right:0;bottom:31px;z-index:1}
.photo--solo{top:0;width:140px;
  background:linear-gradient(90deg,rgba(42,42,64,0) 0%,rgba(42,42,64,.55) 30%,rgba(42,42,64,.8) 60%,rgba(60,50,70,.7) 100%)}
.photo--duo{width:160px;height:150px;
  background:linear-gradient(90deg,rgba(62,82,115,0) 0%,rgba(62,82,115,.6) 25%,rgba(230,228,234,.8) 50%,rgba(62,82,115,.85) 80%,rgba(62,82,115,.9) 100%)}
.photo--duo-tall{top:0;width:170px;height:auto;
  background:linear-gradient(90deg,rgba(62,82,115,0) 0%,rgba(62,82,115,.45) 30%,rgba(230,228,234,.7) 55%,rgba(62,82,115,.85) 85%)}
.photo--hug{width:150px;height:235px;
  background:linear-gradient(90deg,rgba(196,77,127,0) 0%,rgba(196,77,127,.35) 35%,rgba(120,70,110,.55) 60%,rgba(196,77,127,.65) 100%),
             linear-gradient(180deg,rgba(227,234,176,0) 40%,rgba(227,234,176,.9) 100%)}
.tag{position:absolute;left:12px;top:12px;padding:2px 6px;border:1px solid #f1c5d3;border-radius:8px;
  font:700 5px/1 "Poppins",sans-serif;color:var(--rose);letter-spacing:.2px;background:rgba(255,255,255,.5);z-index:2}
.head{position:absolute;left:12px;z-index:2;font:900 23px/1.1 "Playfair Display",serif;color:var(--plum)}
.head em{font-style:normal;color:var(--rose)}
.head--italic{font-style:italic}
.head--italic em{font-style:italic}
.head small{display:block;font-size:14px;line-height:1;margin-top:8px;color:var(--rose)}
.sub{position:absolute;left:0;z-index:2;padding:6px 22px 7px 12px;border-radius:0 28px 28px 0;
  background:rgba(252,218,228,.85);font:700 14px/0.95 "Poppins",sans-serif;color:var(--rose)}
.sub span{display:block;font-size:7px;color:var(--ink);margin-bottom:2px}
.sub--clear{background:none}
.sub--dark{background:var(--plum-bar)}
.sub--dark span{color:var(--white)}
.bar{position:absolute;left:0;bottom:8px;width:100%;height:23px;background:var(--plum-bar);z-index:3;
  display:flex;align-items:center;justify-content:space-between;padding:0 12px}
.bar p{font:700 8px/1 "Poppins",sans-serif;color:var(--rose)}
.bar p b{color:var(--white)}
.stores{display:flex;gap:4px}
.store{width:52px;height:15px;border-radius:3px;background:#000;border:1px solid #bbb}
</style>
</head>
<body>
<main class="board">

<article class="card" style="left:56px;top:58px">
  <div class="photo photo--solo" role="img" aria-label="Photo of the coach standing and smiling in a black outfit"></div>
  <p class="tag">KELMORA . MB IN YOUR POCKET</p>
  <h2 class="head" style="top:42px">Built for<br>Women<br>Who Are<br><em>Tired of<br>Doing This<br>Alone</em></h2>
  <p class="sub" style="top:225px"><span>Stay Consistent with</span>MB in Your<br>Pocket!</p>
  <footer class="bar"><p>Downlode <b>Kelmora</b> App!</p><div class="stores"><i class="store"></i><i class="store"></i></div></footer>
</article>

<article class="card" style="left:332px;top:58px">
  <div class="photo photo--duo" role="img" aria-label="Photo of two women laughing together"></div>
  <p class="tag">KELMORA . MB IN YOUR POCKET</p>
  <h2 class="head" style="top:40px;font-size:21px;line-height:1.05">You Don't Need<br>More Willpower.<br><em>You Need<br>More Support</em></h2>
  <p class="sub sub--clear" style="top:183px"><span>Stay Consistent with</span>MB in Your<br>Pocket!</p>
  <footer class="bar"><p>Downlode <b>Kelmora</b> App!</p><div class="stores"><i class="store"></i><i class="store"></i></div></footer>
</article>

<article class="card" style="left:609px;top:58px">
  <div class="photo photo--hug" role="img" aria-label="Photo of two women hugging and laughing"></div>
  <p class="tag">KELMORA . MB IN YOUR POCKET</p>
  <h2 class="head head--italic" style="top:40px;font-size:25px;line-height:1.05">When<br>Motivation<br>Fades,<small style="font-style:normal">MB Checks In</small></h2>
  <p class="sub sub--clear" style="top:225px"><span>Stay Consistent with</span>MB in Your<br>Pocket!</p>
  <footer class="bar"><p>Downlode <b>Kelmora</b> App!</p><div class="stores"><i class="store"></i><i class="store"></i></div></footer>
</article>

<article class="card" style="left:885px;top:58px">
  <div class="photo photo--solo" role="img" aria-label="Photo of the coach standing and smiling in a black outfit"></div>
  <p class="tag">KELMORA . MB IN YOUR POCKET</p>
  <h2 class="head" style="top:44px">One Bad<br>Meal<br>Doesn't<br>Mean<br><em>You<br>Failed</em></h2>
  <p class="sub sub--dark" style="top:225px"><span>Stay Consistent with</span>MB in Your<br>Pocket!</p>
  <footer class="bar"><p>Downlode <b>Kelmora</b> App!</p><div class="stores"><i class="store"></i><i class="store"></i></div></footer>
</article>

<article class="card" style="left:56px;top:438px">
  <div class="photo photo--solo" role="img" aria-label="Photo of the coach standing and smiling in a black outfit"></div>
  <p class="tag">KELMORA . MB IN YOUR POCKET</p>
  <h2 class="head head--italic" style="top:42px;font-size:25px;line-height:1.08">Stop<br>Starting<br>Over<br><em style="font-style:normal">Every<br>Monday</em></h2>
  <p class="sub sub--clear" style="top:225px"><span>Stay Consistent with</span>MB in Your<br>Pocket!</p>
  <footer class="bar"><p>Downlode <b>Kelmora</b> App!</p><div class="stores"><i class="store"></i><i class="store"></i></div></footer>
</article>

<article class="card" style="left:332px;top:438px">
  <div class="photo photo--hug" role="img" aria-label="Photo of two women hugging and laughing"></div>
  <p class="tag">KELMORA . MB IN YOUR POCKET</p>
  <h2 class="head head--italic" style="top:40px;font-size:25px;line-height:1.05">Eat the food<br>you love.<small style="font-style:normal;margin-top:6px">Stay accountable<br>every day.</small></h2>
  <p class="sub sub--clear" style="top:225px"><span>Stay Consistent with</span>MB in Your<br>Pocket!</p>
  <footer class="bar"><p>Downlode <b>Kelmora</b> App!</p><div class="stores"><i class="store"></i><i class="store"></i></div></footer>
</article>

<article class="card" style="left:609px;top:438px">
  <div class="photo photo--solo" role="img" aria-label="Photo of the coach standing and smiling in a black outfit"></div>
  <p class="tag">KELMORA . MB IN YOUR POCKET</p>
  <h2 class="head" style="top:42px">The<br>Missing<br>Piece<br>Isn't<br><em>Another<br>Diet</em></h2>
  <p class="sub" style="top:226px"><span>Stay Consistent with</span>MB in Your<br>Pocket!</p>
  <footer class="bar"><p>Downlode <b>Kelmora</b> App!</p><div class="stores"><i class="store"></i><i class="store"></i></div></footer>
</article>

<article class="card" style="left:885px;top:438px">
  <div class="photo photo--duo-tall" role="img" aria-label="Photo of two women laughing together by a window"></div>
  <p class="tag">KELMORA . MB IN YOUR POCKET</p>
  <h2 class="head" style="top:42px">The<br>Support<br>System<br><em>You've<br>Been<br>Missing</em></h2>
  <p class="sub sub--clear" style="top:225px"><span>Stay Consistent with</span>MB in Your<br>Pocket!</p>
  <footer class="bar"><p>Downlode <b>Kelmora</b> App!</p><div class="stores"><i class="store"></i><i class="store"></i></div></footer>
</article>

<article class="card" style="left:332px;top:818px">
  <div class="photo photo--solo" role="img" aria-label="Photo of the coach standing and smiling in a black outfit"></div>
  <p class="tag">KELMORA . MB IN YOUR POCKET</p>
  <h2 class="head" style="top:74px;font-size:22px;line-height:1.05">What if MB<br>Checked in<br><em>Every Day?</em></h2>
  <p class="sub sub--dark" style="top:193px"><span>Stay Consistent with</span>MB in Your<br>Pocket!</p>
  <footer class="bar"><p>Downlode <b>Kelmora</b> App!</p><div class="stores"><i class="store"></i><i class="store"></i></div></footer>
</article>

<article class="card" style="left:609px;top:818px">
  <div class="photo photo--hug" role="img" aria-label="Photo of two women hugging and laughing" style="height:240px"></div>
  <p class="tag">KELMORA . MB IN YOUR POCKET</p>
  <h2 class="head head--italic" style="top:36px;font-size:23px;line-height:1.05">Support<br>When<br>Motivation<br><em style="font-style:normal">Disappears</em></h2>
  <p class="sub" style="top:193px"><span>Stay Consistent with</span>MB in Your<br>Pocket!</p>
  <footer class="bar"><p>Downlode <b>Kelmora</b> App!</p><div class="stores"><i class="store"></i><i class="store"></i></div></footer>
</article>

</main>
</body>
</html>
```